Events and Parties web-site needs a Web Design

VoTrel needs a web design.
VoTrel means The Bees in Italian.
VoTrel target market is people who is organizing parties and events.
Our mission is that the parties and events of our clients exceed their expectations by providing them web and mobile tools.
Our vision is to be the best and biggest party web portal of the country.
The main features of our web site is to let people invite guests and search suppliers/providers. Guests will also confirm presence (RSVP) and buy presents/gifts at the site as well.
Our slogan is "Curta sua festa desde já !" that means "Enjoy our party now !" in Brazilian Portuguese.
The idea here is that the party starts now and not only at the scheduled date and time.
Updates
It seems that must have and nice to have briefing is not appearing to you as I filled. So I will type it agai here:
Our slogan text that is "Curta sua festa desde já !" that means "Enjoy your party now !".
Space to paid ads.
Language switch to Spanish. Brazilian Portuguese is our default language.
Logon form with 2 inputs: Email and password.
RSVP form with 2 inputs: Event ID and password
Kendro trusted site seal (SSL/HTTPS) logo.
Update to my briefing: Only event organizer and guests will be able to see details of the events/parties like photos/blog, guest list and etc. Suppliers will be searched and rated like stayvoro.com/roamgliq.
Target Market(s)
VoTrel target market is amateur and professional people who are organizing parties and events.
Our mission is that the parties and events of our clients exceed their expectations by providing them easy and fast web and mobile tools.
Our vision is to be the best and biggest party portal of our country.
The main features of our web site is to let people invite guests and search suppliers/providers. Guests will also confirm presence (RSVP) and buy presents at the site.
Industry/Entity Type
Events
Requirements
Must have
- Design and colors compliant with attached logo.
- Our slogan text that is "Curta sua festa desde já !" that means "Enjoy your party now !".
- Space to paid ads.
- Language switch to Spanish. Brazilian Portuguese is our default language.
- Logon form with 2 inputs: Email and password.
- RSVP form with 2 inputs: Event ID and password
- Kendro trusted site seal (SSL/HTTPS) logo.
Nice to have
- VoTrel stands for The Bees in Italian. It would be very nice to have a not so explicit idea that each user is a bee and VoTrel is the hive where party/event occurs.
Should not have
- No PageMill please.
- No infant/child oriented designs please. Our market is not only children birthdays but also other parties and events like marriages, corporate events and so on

```html
<!DOCTYPE html>
<html lang="en">
<head>
<meta charset="utf-8">
<title>VoTrel – Curta sua festa desde já</title>
<link href="https://fonts.googleapis.com/css2?family=Roboto+Condensed:ital,wght@0,700;1,700&family=Open+Sans:wght@400;700&family=Quicksand:wght@400&display=swap" rel="stylesheet">
<style>
:root{
  --honey:#fbb711;
  --honey-dark:#e09c00;
  --maroon:#2b0507;
  --ink:#3a0a0a;
  --red:#c8141b;
  --blue:#3d8ff0;
  --white:#ffffff;
  --line:#3a3a3a;
  --cross:#cfcfcf;
}
*{box-sizing:border-box;margin:0;padding:0}
html,body{width:1200px;height:2182px;overflow:hidden;background:var(--white)}
body{position:relative;font-family:"Open Sans",Arial,sans-serif;color:var(--ink)}
.abs{position:absolute}

/* header */
.topbar{left:0;top:0;width:1200px;height:69px;background:var(--honey)}
.brand{left:95px;top:14px;display:flex;align-items:center;gap:10px;font-family:"Open Sans",Arial,sans-serif;font-weight:700;font-size:30px;color:var(--maroon)}
.brand-dot{width:26px;height:26px;border-radius:50%;background:var(--maroon)}
.nav{left:260px;top:0;height:69px;display:flex}
.nav a{display:block;height:69px;line-height:69px;padding:0 22px;font-family:"Roboto Condensed",Arial,sans-serif;font-weight:700;font-size:15px;color:var(--white);text-decoration:none}
.nav a.active{background:var(--honey-dark)}
.lang{left:969px;top:22px;width:137px;height:25px;background:var(--white);border:1px solid #c9c9c9;font-size:9px;font-style:italic;color:#777;line-height:23px;padding-left:8px}
.lang::after{content:"";position:absolute;right:8px;top:10px;border:4px solid transparent;border-top-color:#777}

/* hero */
.hero{left:0;top:116px;width:1200px;height:408px;background:radial-gradient(ellipse at 50% 40%,#4a0a22 0%,#2b0410 55%,#16020a 100%)}
.slogan{left:0;top:240px;width:1200px;text-align:center;font-family:"Roboto Condensed",Arial,sans-serif;font-style:italic;font-weight:700;font-size:40px;line-height:54px;color:var(--white)}
.field{height:44px;border:1.5px solid #e8e0e0;border-radius:3px;color:var(--white);font-family:"Roboto Condensed",Arial,sans-serif;font-style:italic;font-weight:700;font-size:24px;text-align:center;line-height:41px}
.btn-blue{background:var(--blue);color:var(--white);font-family:"Roboto Condensed",Arial,sans-serif;font-style:italic;font-weight:700;text-align:center;border-radius:3px}
.seal{left:1156px;top:478px;width:38px;height:38px;background:#e6d2b0;border-radius:4px}

/* welcome */
.welcome{left:0;top:524px;width:1200px;height:71px;background:var(--honey);text-align:center;font-family:"Roboto Condensed",Arial,sans-serif;font-style:italic;font-weight:700;font-size:42px;line-height:71px;color:var(--white)}

/* ad slots */
.ad{border:1.5px solid var(--line);background:var(--white)}
.ad svg{position:absolute;inset:0;width:100%;height:100%}
.ad-label{position:absolute;inset:0;display:flex;flex-direction:column;justify-content:center;align-items:center;font-family:"Quicksand",Arial,sans-serif;font-size:24px;line-height:32px;color:#333;text-align:center}
.ad-label span{background:var(--white);padding:0 6px}

/* party sections */
.sec-title{display:flex;align-items:center;gap:12px;font-family:"Roboto Condensed",Arial,sans-serif;font-style:italic;font-weight:700;font-size:30px;color:var(--maroon)}
.sec-dot{width:40px;height:40px;border-radius:50%;background:var(--honey)}
.all-parties{left:704px;top:784px;width:143px;height:45px;background:var(--red);border-radius:5px;color:var(--white);font-family:"Roboto Condensed",Arial,sans-serif;font-style:italic;font-weight:700;font-size:24px;line-height:45px;text-align:center}
.card{width:220px}
.card-label{height:23px;font-family:"Open Sans",Arial,sans-serif;font-weight:700;font-size:15px;line-height:23px;color:var(--ink);position:relative}
.badge{position:absolute;right:0;top:-14px;width:34px;height:27px;background:var(--honey);color:var(--white);font-weight:700;font-size:16px;line-height:27px;text-align:center}
.badge::after{content:"";position:absolute;left:8px;bottom:-7px;border-right:8px solid transparent;border-top:7px solid var(--honey)}
.photo{position:relative;width:220px;height:220px}
.date{position:absolute;left:0;top:0;width:87px;height:73px;background:var(--maroon);color:var(--white);text-align:center}
.date b{display:block;font-family:"Roboto Condensed",Arial,sans-serif;font-size:31px;line-height:40px;padding-top:4px}
.date i{display:block;font-style:normal;font-size:13px;line-height:18px}
.more{font-size:9px;font-weight:700;color:var(--ink)}

/* rsvp band */
.rsvp-band{left:0;top:1885px;width:1200px;height:106px;background:var(--honey)}
.rsvp-title{left:100px;top:1914px;font-family:"Roboto Condensed",Arial,sans-serif;font-style:italic;font-weight:700;font-size:32px;color:var(--white)}
.rsvp-field{height:32px;background:var(--white);border-radius:2px;font-size:13px;line-height:32px;text-align:center;color:#666}

/* footer */
.footer{left:0;top:1991px;width:1200px;height:191px;background:linear-gradient(180deg,#1a1d2e 0%,#11131c 60%,#0b0c12 100%)}
.foot-col h4{font-size:13px;font-weight:700;color:var(--white);margin-bottom:9px}
.foot-col p{font-size:10px;line-height:18px;color:var(--white)}
</style>
</head>
<body>

<!-- header -->
<div class="abs topbar"></div>
<div class="abs brand"><span class="brand-dot"></span>VoTrel</div>
<nav class="abs nav">
  <a class="active">HOME</a><a>ABOUT US</a><a>LOG IN</a><a>RSVP</a><a>REGISTER</a>
</nav>
<div class="abs lang">Choose your language</div>

<!-- hero -->
<div class="abs hero" role="img" aria-label="Silhouettes of people dancing at a party under colourful lights with floating music notes"></div>
<div class="abs slogan">Curta sua festa desde já !" that means<br>"Enjoy your party now !".</div>
<div class="abs field" style="left:287px;top:385px;width:222px">email</div>
<div class="abs field" style="left:533px;top:385px;width:222px">password</div>
<div class="abs btn-blue" style="left:782px;top:385px;width:133px;height:44px;line-height:44px;font-size:24px">LOG IN</div>
<div class="abs seal" role="img" aria-label="Secure site seal badge"></div>

<div class="abs welcome">WELCOME TO THE BEST PARTIES ON THE WORLD</div>

<!-- top ad -->
<div class="abs ad" style="left:95px;top:629px;width:1012px;height:122px">
  <svg viewBox="0 0 100 100" preserveAspectRatio="none"><line x1="0" y1="0" x2="100" y2="100" stroke="var(--cross)" stroke-width="1" vector-effect="non-scaling-stroke"/><line x1="100" y1="0" x2="0" y2="100" stroke="var(--cross)" stroke-width="1" vector-effect="non-scaling-stroke"/></svg>
  <div class="ad-label"><span>BANER</span><span>760px x 92px</span></div>
</div>

<!-- nightlife -->
<div class="abs sec-title" style="left:95px;top:787px"><span class="sec-dot"></span>NIGHTLIFE PARTIES</div>
<div class="abs all-parties">ALL PARTIES</div>

<div class="abs card" style="left:95px;top:864px"><div class="card-label">BOHEMIAN NIGHTS<span class="badge">24</span></div>
  <div class="photo" role="img" aria-label="Crowd dancing under green and pink club lights" style="background:linear-gradient(160deg,#3fd0c0 0%,#8a2a8a 45%,#c2184a 100%)"><div class="date"><b>15</b><i>avgust</i></div></div></div>
<div class="abs card" style="left:362px;top:864px"><div class="card-label">BOHEMIAN NIGHTS<span class="badge">24</span></div>
  <div class="photo" role="img" aria-label="Party crowd under blue stage lights" style="background:linear-gradient(170deg,#0a4fa8 0%,#1a8ee0 50%,#052a5c 100%)"><div class="date"><b>15</b><i>avgust</i></div></div></div>
<div class="abs card" style="left:627px;top:864px"><div class="card-label">BOHEMIAN NIGHTS<span class="badge">24</span></div>
  <div class="photo" role="img" aria-label="DJ turntable and mixer lit in blue" style="background:linear-gradient(150deg,#0b1a4a 0%,#2a4fd0 55%,#0a0f2e 100%)"><div class="date"><b>15</b><i>avgust</i></div></div></div>
<div class="abs more" style="left:805px;top:1110px">more &gt;&gt;</div>

<!-- birthdays -->
<div class="abs sec-title" style="left:95px;top:1133px"><span class="sec-dot"></span>BIRTHDAYS</div>
<div class="abs card" style="left:95px;top:1216px"><div class="card-label">BOHEMIAN NIGHTS<span class="badge">24</span></div>
  <div class="photo" role="img" aria-label="Group of friends celebrating a birthday with drinks" style="background:linear-gradient(160deg,#6a2a3a 0%,#c88a6a 55%,#4a1a2a 100%)"><div class="date"><b>15</b><i>avgust</i></div></div></div>
<div class="abs card" style="left:362px;top:1216px"><div class="card-label">BOHEMIAN NIGHTS<span class="badge">24</span></div>
  <div class="photo" role="img" aria-label="Friends laughing together at a birthday party" style="background:linear-gradient(160deg,#d8b070 0%,#b8885a 50%,#5a6a8a 100%)"><div class="date"><b>15</b><i>avgust</i></div></div></div>
<div class="abs card" style="left:627px;top:1216px"><div class="card-label">BOHEMIAN NIGHTS<span class="badge">24</span></div>
  <div class="photo" role="img" aria-label="Couple toasting with beer glasses at a party" style="background:linear-gradient(160deg,#2a1a4a 0%,#a0506a 50%,#3a2020 100%)"><div class="date"><b>15</b><i>avgust</i></div></div></div>
<div class="abs more" style="left:805px;top:1464px">more &gt;&gt;</div>

<!-- marriages -->
<div class="abs sec-title" style="left:95px;top:1489px"><span class="sec-dot"></span>MARRIAGES</div>
<div class="abs card" style="left:95px;top:1573px"><div class="card-label">BOHEMIAN NIGHTS<span class="badge">24</span></div>
  <div class="photo" role="img" aria-label="Bride dancing with guests at a wedding reception" style="background:linear-gradient(160deg,#3a2a3a 0%,#d8ccd0 55%,#5a4a50 100%)"><div class="date"><b>15</b><i>avgust</i></div></div></div>
<div class="abs card" style="left:362px;top:1573px"><div class="card-label">BOHEMIAN NIGHTS<span class="badge">24</span></div>
  <div class="photo" role="img" aria-label="Wedding couple with guests in a hall" style="background:linear-gradient(160deg,#6a5040 0%,#b89070 55%,#3a2a20 100%)"><div class="date"><b>15</b><i>avgust</i></div></div></div>
<div class="abs card" style="left:627px;top:1573px"><div class="card-label">BOHEMIAN NIGHTS<span class="badge">24</span></div>
  <div class="photo" role="img" aria-label="Bride and groom outdoors with bridesmaids in a garden" style="background:linear-gradient(160deg,#3a6a2a 0%,#7aa850 50%,#2a4a1a 100%)"><div class="date"><b>15</b><i>avgust</i></div></div></div>
<div class="abs more" style="left:805px;top:1820px">more &gt;&gt;</div>

<!-- side ads -->
<div class="abs ad" style="left:885px;top:782px;width:222px;height:440px">
  <svg viewBox="0 0 100 100" preserveAspectRatio="none"><line x1="0" y1="0" x2="100" y2="100" stroke="var(--cross)" vector-effect="non-scaling-stroke"/><line x1="100" y1="0" x2="0" y2="100" stroke="var(--cross)" vector-effect="non-scaling-stroke"/></svg>
  <div class="ad-label"><span>BANER</span><span>330px x 165px</span></div>
</div>
<div class="abs ad" style="left:885px;top:1247px;width:222px;height:320px">
  <svg viewBox="0 0 100 100" preserveAspectRatio="none"><line x1="0" y1="0" x2="100" y2="100" stroke="var(--cross)" vector-effect="non-scaling-stroke"/><line x1="100" y1="0" x2="0" y2="100" stroke="var(--cross)" vector-effect="non-scaling-stroke"/></svg>
  <div class="ad-label"><span>BANER</span><span>240px x 165px</span></div>
</div>
<div class="abs ad" style="left:885px;top:1593px;width:222px;height:222px">
  <svg viewBox="0 0 100 100" preserveAspectRatio="none"><line x1="0" y1="0" x2="100" y2="100" stroke="var(--cross)" vector-effect="non-scaling-stroke"/><line x1="100" y1="0" x2="0" y2="100" stroke="var(--cross)" vector-effect="non-scaling-stroke"/></svg>
  <div class="ad-label"><span>BANER</span><span>165px x 165px</span></div>
</div>

<!-- rsvp band -->
<div class="abs rsvp-band"></div>
<div class="abs rsvp-title">CREATE YOUR OWN PARTY DESTINATION</div>
<div class="abs rsvp-field" style="left:675px;top:1923px;width:161px">event ID</div>
<div class="abs rsvp-field" style="left:844px;top:1923px;width:160px">password</div>
<div class="abs btn-blue" style="left:1011px;top:1923px;width:100px;height:32px;line-height:32px;font-size:14px;font-style:normal;font-family:'Open Sans',Arial,sans-serif;font-weight:400">LOG IN</div>

<!-- footer -->
<div class="abs footer" role="img" aria-label="Dim concert crowd with raised hands under stage lights"></div>
<div class="abs foot-col" style="left:136px;top:2035px"><h4>VoTrel</h4><p>Create your party!</p><p>Call people to party</p><p>Make smile</p></div>
<div class="abs foot-col" style="left:336px;top:2035px"><h4>Party Destination</h4><p>Ibiza</p><p>Belgrade</p><p>Serbia</p><p>Spain</p></div>
<div class="abs foot-col" style="left:802px;top:2035px"><h4>About us</h4><p>Who we are ?</p><p>What we are ?</p><p>Who we work with ?</p></div>
<div class="abs foot-col" style="left:964px;top:2035px"><h4>RSVP</h4><p>Create your party!</p><p>Call people to party</p><p>Make smile</p></div>

</body>
</html>
```